Landingpage design

We need a landingpage for a chatterloop add campaign. We sell socks made of bamboo in super quality. Our customers loves us, and we have a 5 heart rating at opinivo.com.

We want to create a add campaign targeted new customers, and the offer is that they can buy 1 pair of bamboo socks as a test, for only 20 DKK (2,7 Euro) including shipment. Our webpage is www.lintora.dk, landingpage should be built i Pagmoro, a wysiwyg editor. based on their template. like:
https://lintora.pagmoro.com/13844-sales-page
https://lintora.pagmoro.com/13696-sales-page
https://lintora.pagmoro.com/13845-sales-page

You don't have to follow the templates 100% if you have better ideas. We have an account for snapquarry, so please get stockphotos from here.

Bamboo socks has a lot of great selling points, you can see a good desciption here:
https://tovelin.com/us/why-bamboo

We expect you to have experience in landingpage design, and expect to end up with 2 landingpages we can splittest on.

This is the first of a number of landingpages we need in the future, so for the right person there will be plenty of more work.

Target Market(s)

Denmark

Industry/Entity Type

E-Commerce

Number of Pages Required

2 page

Colors

Designer to choose colors to be used in the design.

Requirements
Must have
• A great selling page, showing all the great things with bamboo socks. It should be supplied with good packshots from snapquarry.com

```html
<!DOCTYPE html>
<html lang="en">
<head>
<meta charset="utf-8">
<title>Lintora – Bamboo Socks</title>
<link href="https://fonts.googleapis.com/css2?family=Roboto:wght@300;400;500;700&display=swap" rel="stylesheet">
<style>
:root{
  --green:#2fb487;
  --green-light:#3fdc9a;
  --green-dark:#239a71;
  --ink:#2b2f36;
  --muted:#7a8089;
  --soft:#f2f2f2;
  --white:#ffffff;
  --blue-top:#6fd6ec;
  --blue-bottom:#5a98ea;
  --footer:#1c2233;
  --star:#f5b82e;
}
*{box-sizing:border-box;margin:0;padding:0}
html,body{width:1200px;height:5367px;overflow:hidden}
body{font-family:'Roboto',sans-serif;color:var(--ink);background:var(--white);position:relative}
section,header,footer{position:absolute;left:0;width:1200px}
.btn{display:inline-block;background:var(--green);color:var(--white);font-size:13px;font-weight:500;letter-spacing:.5px;text-transform:uppercase;text-align:center;line-height:36px;height:36px;border-radius:2px}
.btn-ghost{background:transparent;border:1.5px solid var(--green);color:var(--green);line-height:33px}
.photo{position:absolute}
.small{font-size:11px;color:var(--muted)}

/* header */
.site-header{top:0;height:72px;background:var(--white);border-bottom:1px solid #eee}
.brand{position:absolute;left:134px;top:14px;display:flex;align-items:center;gap:10px}
.brand-square{width:40px;height:40px;background:var(--ink)}
.brand-name{font-size:18px;font-weight:700;color:var(--ink)}
.brand-tag{font-size:11px;color:var(--muted);display:block;font-weight:400}
.nav{position:absolute;left:484px;top:27px;display:flex;gap:48px;font-size:12px;text-transform:uppercase;color:var(--muted)}
.nav .active{color:var(--ink);border-bottom:2px solid var(--green);padding-bottom:4px}
.site-header .btn{position:absolute;left:908px;top:20px;width:160px;height:32px;line-height:32px;font-size:11px}

/* hero */
.hero{top:72px;height:470px;background:var(--soft)}
.headline{position:absolute;left:134px;top:96px;font-size:41px;line-height:48px;font-weight:500;color:var(--ink);white-space:nowrap}
.checks{position:absolute;left:134px;top:212px;list-style:none;font-size:15px;color:var(--muted)}
.checks li{display:flex;align-items:center;gap:10px;height:27px;white-space:nowrap}
.hero .actions{position:absolute;left:134px;top:318px;display:flex;gap:18px}
.hero .actions .btn{width:190px}
.hero .small{position:absolute;left:134px;top:368px}

/* why */
.why{top:542px;height:518px;background:linear-gradient(180deg,var(--green),var(--green-light));color:var(--white);text-align:center}
.why h2{margin-top:110px;font-size:34px;font-weight:500}
.why .lead{width:640px;margin:24px auto 0;font-size:14px;line-height:22px;font-weight:500}
.cards{position:absolute;left:134px;top:271px;width:932px;display:flex;gap:8px}
.card{flex:1;height:134px;background:var(--soft);padding:22px 18px;color:var(--muted)}
.card h3{font-size:16px;font-weight:500;color:var(--ink);margin-bottom:14px}
.card p{font-size:11px;line-height:17px}

/* features */
.features{top:1060px;height:1152px;background:var(--white)}
.feature h3{position:absolute;font-size:27px;font-weight:500}
.feature p{position:absolute;width:420px;font-size:14px;line-height:22px;color:var(--muted)}

/* discount */
.discount{top:2212px;height:390px;background:var(--soft);text-align:center}
.discount .big{margin-top:60px;font-size:84px;font-weight:500;color:var(--green);line-height:96px}
.discount h2{font-size:24px;font-weight:500;line-height:32px;margin-top:10px}
.discount .btn{width:190px;margin-top:24px}
.discount .small{margin-top:10px}

/* facts */
.facts{top:2602px;height:560px;background:linear-gradient(180deg,var(--blue-top),var(--blue-bottom));color:var(--white);text-align:center}
.facts h2{margin-top:98px;font-size:36px;font-weight:500}
.facts .lead{width:600px;margin:22px auto 0;font-size:14px;line-height:22px;font-weight:500}
.fact-row{position:absolute;top:280px;left:176px;width:848px;display:flex;justify-content:space-between}
.fact{width:240px}
.fact .icon{width:86px;height:86px;border-radius:50%;background:var(--white);margin:0 auto 28px;display:flex;align-items:center;justify-content:center}
.fact p{font-size:14px;line-height:22px}

/* video */
.video{top:3162px;height:723px;background:var(--white);text-align:center}
.video h2{margin-top:112px;font-size:36px;font-weight:500}
.video .lead{width:560px;margin:20px auto 0;font-size:14px;line-height:22px;color:var(--muted)}
.ribbon{position:absolute}

/* reviews */
.reviews{top:3885px;height:795px;background:var(--soft);text-align:center}
.stars{margin-top:105px;display:flex;justify-content:center;gap:4px}
.reviews h2{margin-top:10px;font-size:36px;font-weight:500}
.reviews .lead{margin-top:18px;font-size:14px;line-height:22px;color:var(--muted)}
.review-row{position:absolute;left:160px;top:325px;width:880px;display:flex;gap:30px}
.review{flex:1;height:270px;background:var(--white);padding:26px 26px;text-align:left}
.review .who{display:flex;align-items:center;gap:12px;margin-bottom:22px}
.avatar{width:40px;height:40px;border-radius:50%;background:#c9b8a5}
.review .name{font-size:14px;color:var(--ink)}
.review p{font-size:13px;line-height:21px;color:var(--muted)}
.arrow{position:absolute;top:440px}
.reviews .btn{position:absolute;left:486px;top:675px;width:228px}

/* offer */
.offer{top:4680px;height:434px;background:var(--white)}
.offer .headline{top:76px}
.offer .checks{top:192px}
.offer .btn{position:absolute;left:134px;top:296px;width:190px}
.offer .small{position:absolute;left:134px;top:346px}

/* footer */
.site-footer{top:5114px;height:253px;background:var(--footer);color:var(--white)}
.fcol{position:absolute;top:60px}
.fcol h4{font-size:17px;font-weight:500;margin-bottom:16px}
.fcol p{font-size:12px;line-height:19px;color:#c7ccd6}
.footer-links{display:flex;gap:14px;font-size:12px;color:#c7ccd6}
.social-dot{width:18px;height:18px;border-radius:50%;background:var(--white);margin-top:14px}
</style>
</head>
<body>

<header class="site-header">
  <div class="brand"><span class="brand-square"></span><span class="brand-name">Lintora<span class="brand-tag">Fabric i bambus - lige til og enkelt</span></span></div>
  <nav class="nav"><span class="active">Home</span><span>Why Bamboo</span><span>About us</span><span>Reviews</span></nav>
  <a class="btn">Buy now</a>
</header>

<section class="hero">
  <h1 class="headline">Enjoy Your First Pair of Bamboo<br>Socks for Only 20 PKK</h1>
  <ul class="checks">
    <li><svg width="14" height="14" viewBox="0 0 14 14"><path d="M2 7l3 3 7-7" stroke="#2fb487" stroke-width="2" fill="none"/></svg>We have been working on textile for more than 10 years</li>
    <li><svg width="14" height="14" viewBox="0 0 14 14"><path d="M2 7l3 3 7-7" stroke="#2fb487" stroke-width="2" fill="none"/></svg>All products meet our high quality standards</li>
    <li><svg width="14" height="14" viewBox="0 0 14 14"><path d="M2 7l3 3 7-7" stroke="#2fb487" stroke-width="2" fill="none"/></svg>Our customers loves us, and we have a 5 stars rating at opinivo.com</li>
  </ul>
  <div class="actions"><a class="btn">Buy now</a><a class="btn btn-ghost">&#9654;&nbsp; Watch video</a></div>
  <p class="small">Shipment included</p>
  <div class="photo" role="img" aria-label="Man in a green bamboo tank top and briefs" style="left:830px;top:0;width:270px;height:470px;background:linear-gradient(180deg,#d9c3ad 0%,#c8ad93 30%,#2f9a6e 40%,#1f7e58 100%)"></div>
</section>

<section class="why">
  <h2>Why Bamboo Clothing?</h2>
  <p class="lead">It was only in 2011 that the Eastfield University discovered how you can make fabric from bamboo stems. Now bamboo has the potential to become the textile of the future.</p>
  <div class="cards">
    <div class="card"><h3>Comfortable</h3><p>Bamboo fabric breathes, making you comfortable in garments made on this.</p></div>
    <div class="card"><h3>Eco-friendly</h3><p>Bamboo is a very fast growing tropical forest product which does not require the use of pesticides.</p></div>
    <div class="card"><h3>Exquisitely soft</h3><p>The moment you wear it next to your skin you will notice the difference between other fabrics.</p></div>
    <div class="card"><h3>Thermo-control</h3><p>Bamboo fabric is warm, durable in its fibres smoothness, yet is also breathable.</p></div>
  </div>
</section>

<section class="features">
  <div class="feature">
    <div class="photo" role="img" aria-label="Grey knitted bamboo socks laid on a dark surface" style="left:134px;top:107px;width:419px;height:250px;background:linear-gradient(135deg,#3b3d41,#8c8f93 60%,#6b4a5a)"></div>
    <h3 style="left:608px;top:162px">Strong Material</h3>
    <p style="left:608px;top:210px">Bamboo fabric is lightweight yet strong. The natural processing of these bamboos allows the fibre to remain strong to produce an extremely high quality product. This process gives a material that is very durable.</p>
  </div>
  <div class="feature">
    <h3 style="left:134px;top:502px">Completely Clean</h3>
    <p style="left:134px;top:550px">Bamboo fibers doesnt undergo much chemical processing to make the fabric, so you can easily wear it without causing any allergic irritation to the skin that is more prevalent with heavily processed fabrics.</p>
    <div class="photo" role="img" aria-label="Person in dark clothing sitting with bare feet" style="left:643px;top:451px;width:423px;height:249px;background:linear-gradient(135deg,#1d2230,#3a3f4e 60%,#c9a995)"></div>
  </div>
  <div class="feature">
    <div class="photo" role="img" aria-label="Pair of light grey bamboo socks on a dark background" style="left:134px;top:798px;width:419px;height:249px;background:linear-gradient(135deg,#4a4d52,#9a9ca0 55%,#d6d6d6)"></div>
    <h3 style="left:608px;top:855px">Water Absorbent</h3>
    <p style="left:608px;top:903px">Bamboo fibres are water absorbent. So if you live in a humid environment this is the fabric for you. Think of the sweat it will absorb and evaporate out of your body.</p>
  </div>
</section>

<section class="discount">
  <div class="big">-90%</div>
  <h2>Get Your First Pair of Socks With<br>an Exclusive Discount</h2>
  <a class="btn">Buy now</a>
  <p class="small">Shipment included</p>
</section>

<section class="facts">
  <h2>A Few Facts About Lintora</h2>
  <p class="lead">We have been working on textile for more than 10 years. This ensures that all products meet our high quality standards.</p>
  <div class="fact-row">
    <div class="fact"><div class="icon"><svg width="34" height="34" viewBox="0 0 34 34"><path d="M11 4l-8 5 3 6 4-2v17h14V13l4 2 3-6-8-5c-1 3-3 4-6 4s-5-1-6-4z" fill="#5aa8e8"/></svg></div><p>Our mission is to give our customers access to quality products at a reasonable price.</p></div>
    <div class="fact"><div class="icon"><svg width="34" height="34" viewBox="0 0 34 34"><path d="M13 3h8v4l4 4v20H9V11l4-4z" fill="#5aa8e8"/></svg></div><p>We know that the properties of bamboo are absolutely amazing and can reduce, for example, sweaty and your toes.</p></div>
    <div class="fact"><div class="icon"><svg width="34" height="34" viewBox="0 0 34 34"><circle cx="17" cy="13" r="9" fill="#5aa8e8"/><path d="M11 20l-3 11 9-4 9 4-3-11z" fill="#5aa8e8"/></svg></div><p>We shop directly with the factories. This ensures the highest quality at a competitive price.</p></div>
  </div>
</section>

<section class="video">
  <h2>A Short Video About Our Work</h2>
  <p class="lead">We sell stockings, t-shirts, sweaters and more boxershorts. If you choose our subscription service, the products will come to you automatically.</p>
  <svg class="ribbon" style="left:0;top:318px" width="200" height="60" viewBox="0 0 200 60"><path d="M0 10h190l-16 20 16 20H0z" fill="#2fb487"/></svg>
  <svg class="ribbon" style="left:1000px;top:318px" width="200" height="60" viewBox="0 0 200 60"><path d="M200 10H10l16 20-16 20h174z" fill="#2fb487"/></svg>
  <div class="photo" role="img" aria-label="Flat lay of packed clothes, shoes and a suitcase" style="left:296px;top:282px;width:608px;height:333px;background:linear-gradient(135deg,#eceff1,#c7cdd3 45%,#d8c2a6)"></div>
  <svg style="position:absolute;left:570px;top:418px" width="60" height="60" viewBox="0 0 60 60"><circle cx="30" cy="30" r="30" fill="#2fb487"/><path d="M24 18l18 12-18 12z" fill="#fff"/></svg>
</section>

<section class="reviews">
  <div class="stars">
    <svg width="26" height="26" viewBox="0 0 24 24"><path d="M12 2l3 7 7 .6-5.4 4.7 1.7 7.2L12 17.8 5.7 21.5l1.7-7.2L2 9.6 9 9z" fill="#f5b82e"/></svg>
    <svg width="26" height="26" viewBox="0 0 24 24"><path d="M12 2l3 7 7 .6-5.4 4.7 1.7 7.2L12 17.8 5.7 21.5l1.7-7.2L2 9.6 9 9z" fill="#f5b82e"/></svg>
    <svg width="26" height="26" viewBox="0 0 24 24"><path d="M12 2l3 7 7 .6-5.4 4.7 1.7 7.2L12 17.8 5.7 21.5l1.7-7.2L2 9.6 9 9z" fill="#f5b82e"/></svg>
    <svg width="26" height="26" viewBox="0 0 24 24"><path d="M12 2l3 7 7 .6-5.4 4.7 1.7 7.2L12 17.8 5.7 21.5l1.7-7.2L2 9.6 9 9z" fill="#f5b82e"/></svg>
    <svg width="26" height="26" viewBox="0 0 24 24"><path d="M12 2l3 7 7 .6-5.4 4.7 1.7 7.2L12 17.8 5.7 21.5l1.7-7.2L2 9.6 9 9z" fill="#f5b82e"/></svg>
  </div>
  <h2>We Have a 5 Stars Rating</h2>
  <p class="lead">You're in a good company. Here are some important facts<br>and testimonials about us.</p>
  <svg class="arrow" style="left:100px" width="14" height="24" viewBox="0 0 14 24"><path d="M12 2L2 12l10 10" stroke="#2fb487" stroke-width="2.5" fill="none"/></svg>
  <svg class="arrow" style="left:1086px" width="14" height="24" viewBox="0 0 14 24"><path d="M2 2l10 10L2 22" stroke="#2fb487" stroke-width="2.5" fill="none"/></svg>
  <div class="review-row">
    <div class="review"><div class="who"><span class="avatar" role="img" aria-label="Reviewer portrait"></span><div><div class="name">Nora Lindqvist</div><span style="color:#f5b82e;font-size:13px">★★★★★</span></div></div><p>The socks are so soft and they keep my feet dry all day long. I ordered the test pair and now I have a full drawer of them. Great service and fast shipping.</p></div>
    <div class="review"><div class="who"><span class="avatar" role="img" aria-label="Reviewer portrait"></span><div><div class="name">Nora Lindqvist</div><span style="color:#f5b82e;font-size:13px">★★★★★</span></div></div><p>The socks are so soft and they keep my feet dry all day long. I ordered the test pair and now I have a full drawer of them. Great service and fast shipping.</p></div>
    <div class="review"><div class="who"><span class="avatar" role="img" aria-label="Reviewer portrait"></span><div><div class="name">Nora Lindqvist</div><span style="color:#f5b82e;font-size:13px">★★★★★</span></div></div><p>The socks are so soft and they keep my feet dry all day long. I ordered the test pair and now I have a full drawer of them. Great service and fast shipping.</p></div>
  </div>
  <a class="btn">More reviews</a>
</section>

<section class="offer">
  <h1 class="headline">Get Your First Pair of Bamboo<br>Socks for Only 20 PKK</h1>
  <ul class="checks">
    <li><svg width="14" height="14" viewBox="0 0 14 14"><path d="M2 7l3 3 7-7" stroke="#2fb487" stroke-width="2" fill="none"/></svg>Powerfully insulating - keeps you cooler in summer and warmer in winter</li>
    <li><svg width="14" height="14" viewBox="0 0 14 14"><path d="M2 7l3 3 7-7" stroke="#2fb487" stroke-width="2" fill="none"/></svg>Antibacterial - keeps you odor free and feeling and smelling fresh</li>
    <li><svg width="14" height="14" viewBox="0 0 14 14"><path d="M2 7l3 3 7-7" stroke="#2fb487" stroke-width="2" fill="none"/></svg>Most eco-friendly fabric on the planet - help save your planet</li>
  </ul>
  <a class="btn">Buy now</a>
  <p class="small">Shipment included</p>
  <div class="photo" role="img" aria-label="Woman in a green bamboo tank top and briefs" style="left:795px;top:40px;width:290px;height:394px;background:linear-gradient(180deg,#e6cfa0 0%,#d8bfa3 30%,#3aa77b 42%,#2a8d65 100%)"></div>
</section>

<footer class="site-footer">
  <div class="fcol" style="left:134px;width:240px"><h4>About us</h4><p>At Lintora we specialise in basic products in bamboo. We sell stockings, t-shirts, sweaters and men's boxershorts.</p><div class="social-dot" role="img" aria-label="chatterloop"></div></div>
  <div class="fcol" style="left:450px;width:240px"><h4>Contact us</h4><p>Any questions? Then e-mail info@lintora.dk<br>or call us at +45 20 11 48 36</p><p style="margin-top:10px">Or send us a letter to Lintora<br>Kornvej 12<br>8000 Aarhus</p></div>
  <div class="fcol" style="left:766px;width:300px"><h4>Navigation</h4><div class="footer-links"><span>Home</span><span>Why Bamboo</span><span>About</span><span>Reviews</span></div></div>
</footer>

</body>
</html>
```